CTWI application splash screen

We need a 1024x768 image for use as an application splash screen.
The image will be displayed full screen on an 10 inch industrial PC 1024x768 screen while our application is launching. The image should convey that the application is "Waiting for connection to Wi-Fi access point..." and include a graphic of the industrial PC connected to the access point via an Ethernet cable. A list of troubleshooting steps should be included at the bottom of the image. The troubleshooting steps should not be the main focus of the image and should be shown in a smaller font (but still readable at 1024x768 displayed on a 10 inch screen).
I will include a mock up of the general idea of what we are looking for as well as image files for the industrial PC, a screenshot of our application to show on the PC's screen and the AP.
For general look and feel and a sense of corporate branding please review our website https://corvanetillageworks.com/. The splash screen should reflect corporate branding.
Target Market(s)
Users of our application
Industry/Entity Type
Agriculture

```html
<!DOCTYPE html>
<html lang="en">
<head>
<meta charset="utf-8">
<title>CTWI – Waiting for Wi-Fi access point</title>
<link href="https://fonts.googleapis.com/css2?family=Lexend:wght@400;500;600&display=swap" rel="stylesheet">
<style>
:root{
  --field-green:#40b961;
  --panel-green:#58ab2b;
  --white:#ffffff;
  --ink:#111111;
  --device-frame:#2a2a2c;
  --device-screen:#e9eef0;
  --ap-body:#eef0f0;
}
*{margin:0;padding:0;box-sizing:border-box}
html,body{width:1024px;height:768px;overflow:hidden}
body{background:var(--field-green);font-family:"Lexend",sans-serif;color:var(--white)}
.splash{position:relative;width:1024px;height:768px}
.brand{position:absolute;left:33px;top:36px}
.brand-name{font-size:50px;font-weight:600;letter-spacing:4px;line-height:1}
.brand-sub{font-size:16px;font-weight:400;margin-top:10px;line-height:1.1}
.headline{position:absolute;left:172px;top:30px;width:680px;text-align:center;font-size:62px;font-weight:500;line-height:70px;white-space:nowrap}
.diagram{position:absolute;left:0;top:0}
.label{position:absolute;text-align:center;font-weight:500;line-height:1.1;white-space:nowrap}
.label-pc{left:40px;top:442px;width:230px;font-size:25px}
.label-cable{left:398px;top:366px;width:300px;font-size:24px}
.label-ap{left:682px;top:440px;width:340px;font-size:28px}
.label-ap small{display:block;font-size:17px;margin-top:1px}
.troubleshoot{position:absolute;left:28px;top:538px;width:970px;height:202px;background:var(--panel-green);border:2px solid var(--white);padding:4px 20px}
.troubleshoot h2{font-size:24px;font-weight:500;margin-bottom:8px}
.troubleshoot ul{list-style:none;font-size:14.5px;line-height:19.5px}
.troubleshoot li::before{content:"• "}
.troubleshoot ul ul{padding-left:50px}
.troubleshoot ul ul li{padding-left:16px;text-indent:-16px}
.troubleshoot ul ul li::before{content:"→ ";font-size:11px}
</style>
</head>
<body>
<main class="splash">
  <div class="brand">
    <div class="brand-name">CTWI</div>
    <div class="brand-sub">Corvane Tillage Works Inc.</div>
  </div>

  <h1 class="headline">Waiting for<br>connection to Wi-Fi<br>access point...</h1>

  <svg class="diagram" width="1024" height="768" viewBox="0 0 1024 768">
    <polyline points="272,408 948,408 948,392" fill="none" stroke="var(--ink)" stroke-width="4"/>
    <g role="img" aria-label="Tractor cab industrial PC showing the seeding application screen">
      <rect x="20" y="237" width="256" height="200" rx="14" fill="var(--device-frame)"/>
      <rect x="40" y="256" width="226" height="156" fill="var(--device-screen)"/>
    </g>
    <rect role="img" aria-label="Outdoor Wi-Fi access point" x="930" y="220" width="34" height="172" rx="6" fill="var(--ap-body)"/>
  </svg>

  <div class="label label-pc">Tractor cab<br>computer</div>
  <div class="label label-cable">Ethernet cable</div>
  <div class="label label-ap">Wi-Fi Access Point<small>Relaylink RX-220 Outdoor</small></div>

  <section class="troubleshoot">
    <h2>Troubleshooting steps:</h2>
    <ul>
      <li>This screen should only be visible for a short time on boot.</li>
      <li>If this screen stays visible for more than a minute:
        <ul>
          <li>Verify that the Wi-Fi Access Point (AP) powers up when this system does (indicated by a green light on the side of the AP).</li>
          <li>Check the Ethernet cable between this system and the AP for damage, and replace it if necessary.</li>
          <li>Power-cycle this system and wait for it to reboot fully.</li>
          <li>If the issue persists, contact CTWI support for further assistance.</li>
        </ul>
      </li>
    </ul>
  </section>
</main>
</body>
</html>
```